Trendy Interior Design Company Postcard

We're looking to create a 4x6 or 5x7 double sided postcard type of flyer with our Logo on the front and some photos and information on the back. We would like it to capture peoples attention and to communicate that we are a trendy interior design/build company that can take on a diverse variety of projects to suit any type of client.
We have many more photos of projects, if needed.

Target Market(s)

High end residential home renovations and builds.

Industry/Entity Type

It Company

Font styles to use
Serif
Sans Serif

Requirements
Must have
• Our logo on the front, and on the back we want a variety of photos of our jobs, We would like our company contact information: 555-238-9047 - info@quorvel.ca and something to entice potential clients to contact us, such as " Call for your quote today"
Nice to have
• Diversity in designs. As many photos as possible without looking too busy. We want it to look clean, sleek, and neat. Colours should match our website and logo.
Should not have
• Too much colour. No tacky/unprofessional looking fonts.

```html
<!DOCTYPE html>
<html lang="en">
<head>
<meta charset="utf-8">
<title>Quorvel Homes Postcard</title>
<link href="https://fonts.googleapis.com/css2?family=Questrial&display=swap" rel="stylesheet">
<style>
  :root{
    --bg:#e6e6e4;
    --card:#f4f4f3;
    --white:#ffffff;
    --ink:#161a18;
    --tile:#e7e8e9;
    --tile-soft:#eeeeef;
    --accent:#f0bf57;
    --muted:#5a5d5c;
  }
  *{box-sizing:border-box;margin:0;padding:0}
  html,body{width:1200px;height:1200px;overflow:hidden;background:var(--bg)}
  body{position:relative;font-family:"Questrial",sans-serif;color:var(--ink)}
  .card{position:absolute;left:180px;width:840px;height:560px;overflow:hidden;box-shadow:0 6px 24px rgba(0,0,0,.12)}
  .card-front{top:20px;background:var(--white)}
  .card-back{top:620px;background:var(--card)}
  .abs{position:absolute}

  /* front */
  .brand-name{position:absolute;left:0;right:0;top:250px;text-align:center;font-family:"Questrial",sans-serif;font-size:44px;letter-spacing:1px;color:var(--ink)}
  .vertical{position:absolute;font-size:10px;color:var(--muted);writing-mode:vertical-rl;line-height:1.4}
  .licence{left:36px;bottom:40px;transform:rotate(180deg)}
  .site-tag{right:26px;top:30px}

  /* back */
  .back-logo{left:30px;top:92px;font-size:12px;color:var(--ink)}
  .headline{left:160px;top:78px;font-size:28px;font-weight:700;line-height:1.15;letter-spacing:-.3px}
  .contact{left:620px;top:18px;width:200px;height:120px;background:var(--ink);color:var(--white);padding:26px 20px;text-align:center}
  .contact .phone{font-size:17px;letter-spacing:.5px}
  .contact .small{font-size:10px;margin-top:6px;opacity:.9}
  .tile{background:var(--tile);display:flex;align-items:center;justify-content:center;font-size:14px;text-align:center}
  .tile.soft{background:var(--tile-soft)}
  .tile.dark{background:var(--ink);color:var(--white)}
  .tile.small{font-size:11px}
  .quote{left:470px;top:60px;width:150px;height:80px}
  .photo{position:absolute}
  .photo-dining{left:30px;top:230px;width:470px;height:310px;background:linear-gradient(135deg,#7a7570 0%,#b9b2a6 40%,#5a4f48 75%,#3b3431 100%)}
  .photo-kitchen{left:500px;top:140px;width:320px;height:250px;background:linear-gradient(160deg,#d8d4cf 0%,#8b8580 45%,#a66a5e 65%,#6d6f74 100%)}
  .plan{left:30px;top:190px;width:150px;height:120px}
  .design{left:250px;top:380px;width:150px;height:110px}
  .media{left:30px;top:480px;width:150px;height:80px;font-size:15px}
  .social{left:250px;top:490px;width:220px;height:70px;flex-direction:column;gap:4px;font-size:11px}
  .social .sub{font-size:8px;color:var(--muted)}
  .tagline{left:380px;top:165px;width:150px;height:90px;font-size:12px;line-height:1.4;letter-spacing:.5px;padding:0 12px}
  .promise{left:440px;top:255px;width:270px;height:100px;background:var(--accent);padding:14px 16px;font-size:13px;font-weight:700;line-height:1.35;text-align:center}
  .build{left:710px;top:230px;width:110px;height:90px}
  .modern{left:570px;top:360px;width:140px;height:75px}
  .classic{left:710px;top:360px;width:110px;height:80px}
  .story{left:470px;top:440px;width:350px;height:100px;background:var(--tile-soft);padding:16px 18px;font-size:10.5px;line-height:1.5;color:var(--ink)}
</style>
</head>
<body>

<section class="card card-front">
  <span class="vertical site-tag">quorvel.ca</span>
  <p class="brand-name">Quorvel Homes Inc</p>
  <p class="vertical licence">Fully licensed and insured. City of Toronto<br>Licence #B4-7750X</p>
</section>

<section class="card card-back">
  <p class="abs back-logo">Quorvel Homes</p>
  <h1 class="abs headline">The interior design of<br>Quorvel Homes</h1>

  <div class="abs tile soft small quote">Call for your quote<br>today</div>
  <div class="abs contact">
    <div class="phone">555-238-9047</div>
    <div class="small">E-mail: info@quorvel.ca</div>
    <div class="small">www.quorvel.ca</div>
  </div>

  <div class="photo photo-kitchen" role="img" aria-label="Photo of a bright modern kitchen with bar stools"></div>
  <div class="photo photo-dining" role="img" aria-label="Photo of a dining room with a glass table and place settings"></div>

  <div class="abs tile plan">Plan</div>
  <div class="abs tile dark tagline">FROM DESIGN PROJECT TO EXECUTION</div>
  <div class="abs promise">We'll guide you through the maze of styles and possibilities. Together, we'll choose how to make it both attractive and functional.</div>
  <div class="abs tile build">Build</div>
  <div class="abs tile soft small modern">Modern style</div>
  <div class="abs tile soft small classic">Classic style</div>
  <div class="abs tile design">Design</div>
  <div class="abs tile dark media">Media</div>
  <div class="abs tile soft social">
    <span>Find us on social media</span>
    <span class="sub">Follow · Share · Connect</span>
  </div>
  <p class="abs story">Every new Quorvel Homes project begins with… a cup of fragrant tea or invigorating coffee. So, while talking about it, we choose among the variety of paths and options the one and only which satisfy all the client's wishes.</p>
</section>

</body>
</html>
```